agricultural technology company needs business cards*

design a business card that represents our business well. please see our website: vastrelbyfieldseal.com.au
professional, simple, clean lines, not complicated or floral.....

```html
<!DOCTYPE html>
<html lang="en">
<head>
<meta charset="utf-8">
<title>Vastrel Byfieldseal — Business Card</title>
<link rel="stylesheet" href="https://fonts.googleapis.com/css2?family=Source+Sans+3:wght@400;600&display=swap">
<style>
  :root {
    --backdrop: #e9e7e2;
    --card-white: #ffffff;
    --card-black: #151515;
    --lime: #a6d23a;
    --green: #22b04b;
    --navy: #2f3f7a;
    --leaf-text: #7bbf3a;
    --ink: #3a3a3a;
    --card-w: 620px;
    --card-h: 354px;
  }
  * { box-sizing: border-box; margin: 0; padding: 0; }
  html, body {
    width: 771px; height: 1200px; overflow: hidden;
    background: var(--backdrop);
    font-family: "Source Sans 3", "Helvetica Neue", Arial, sans-serif;
  }
  .sheet {
    width: 771px; height: 1200px;
    display: flex; flex-direction: column; align-items: center; justify-content: center;
    gap: 110px;
  }
  .card {
    position: relative;
    width: var(--card-w); height: var(--card-h);
    border-radius: 4px; overflow: hidden;
    box-shadow: 0 10px 28px rgba(0,0,0,.22);
  }
  .card--front { background: var(--card-white); }
  .card--back { background: var(--card-black); display: flex; align-items: center; justify-content: center; }
  .corner-band { position: absolute; inset: 0; width: 100%; height: 100%; }
  .holder { position: absolute; left: 44px; top: 178px; }
  .holder__name {
    color: var(--navy); font-weight: 400; font-size: 25px; letter-spacing: .04em;
    text-transform: uppercase; line-height: 1.1;
  }
  .holder__role {
    color: var(--leaf-text); font-size: 13px; letter-spacing: .05em;
    text-transform: uppercase; margin-top: 3px;
  }
  .contacts { list-style: none; margin-top: 20px; }
  .contacts li {
    display: flex; align-items: center; gap: 12px;
    color: var(--ink); font-size: 14.5px; line-height: 24px;
  }
  .contacts svg { width: 13px; height: 13px; fill: var(--lime); flex: none; }
  .brand { display: flex; align-items: center; gap: 16px; }
  .brand__mark { width: 22px; height: 22px; background: var(--green); }
  .brand__name { color: var(--green); font-weight: 600; font-size: 44px; letter-spacing: .01em; }
</style>
</head>
<body>
<main class="sheet">
  <section class="card card--front" aria-label="Business card front">
    <svg class="corner-band" viewBox="0 0 620 354" preserveAspectRatio="none" aria-hidden="true">
      <defs>
        <linearGradient id="bandGrad" x1="0" y1="0" x2="1" y2="0">
          <stop offset="0" stop-color="#a6d23a"/>
          <stop offset="1" stop-color="#22b04b"/>
        </linearGradient>
      </defs>
      <polygon points="0,0 620,0 620,92 370,158 0,118" fill="url(#bandGrad)"/>
    </svg>
    <div class="holder">
      <h1 class="holder__name">Maren Oakhurst</h1>
      <p class="holder__role">Director, Vastrel Byfieldseal</p>
      <ul class="contacts">
        <li><svg viewBox="0 0 24 24"><path d="M6.6 10.8a15 15 0 0 0 6.6 6.6l2.2-2.2c.3-.3.7-.4 1-.2 1.1.4 2.3.6 3.6.6.6 0 1 .4 1 1V20c0 .6-.4 1-1 1A17 17 0 0 1 3 4c0-.6.4-1 1-1h3.5c.6 0 1 .4 1 1 0 1.3.2 2.5.6 3.6.1.3 0 .7-.2 1z"/></svg>1300 482 613</li>
        <li><svg viewBox="0 0 24 24"><circle cx="12" cy="12" r="10"/></svg>vastrelbyfieldseal.com.au</li>
        <li><svg viewBox="0 0 24 24"><path d="M2 5h20v14H2z"/></svg>hello@vastrelbyfieldseal.com.au</li>
        <li><svg viewBox="0 0 24 24"><path d="M12 2a7 7 0 0 0-7 7c0 5 7 13 7 13s7-8 7-13a7 7 0 0 0-7-7z"/></svg>12 Tallowfield Lane, Brindlemoor</li>
      </ul>
    </div>
  </section>

  <section class="card card--back" aria-label="Business card back">
    <div class="brand">
      <span class="brand__mark" aria-hidden="true"></span>
      <span class="brand__name">Vastrel Byfieldseal</span>
    </div>
  </section>
</main>
</body>
</html>
```